Criação de Kit com 6 Layouts de Post para Redes Sociais (Facebook, Instagram e etc) + Capa de Facebook para Advocacia e Direito
A empresa queria:
" O escritório atua na área previdênciaria "

```html
<!DOCTYPE html>
<html lang="pt-BR">
<head>
<meta charset="utf-8">
<title>Direito Previdenciário – Post</title>
<link rel="stylesheet" href="https://fonts.googleapis.com/css2?family=Cinzel:wght@500&family=Montserrat:wght@400;500&display=swap">
<style>
  :root{
    --bg:#ffffff;
    --gold:#8c6a40;
    --gold-dark:#5a3f24;
    --gold-light:#c9ad8a;
    --text:#2e2e2e;
    --photo-top:#7d9a5a;
    --photo-bottom:#b8ab94;
  }
  html,body{margin:0;padding:0;overflow:hidden;background:var(--bg);}
  .post{position:relative;width:1200px;height:1200px;overflow:hidden;background:var(--bg);}
  .backdrop{
    position:absolute;left:0;top:0;width:1200px;height:1200px;
    background:
      radial-gradient(ellipse 620px 520px at 280px 330px, rgba(200,196,190,.85), rgba(230,228,225,.5) 55%, rgba(255,255,255,0) 80%),
      linear-gradient(90deg, #e4e2de 0%, #f3f2f0 45%, #ffffff 70%);
  }
  .accent-square{
    position:absolute;left:132px;top:458px;width:392px;height:478px;
    border-radius:0 22px 22px 22px;
    background:linear-gradient(180deg,var(--gold-dark) 0%, #7a5a38 45%, var(--gold-light) 100%);
  }
  .accent-dots{position:absolute;left:60px;top:500px;}
  .hero-photo{
    position:absolute;left:160px;top:70px;width:298px;height:806px;
    background:linear-gradient(180deg, var(--photo-top) 0%, #a3ad90 45%, var(--photo-bottom) 100%);
  }
  .headline{
    position:absolute;left:580px;top:270px;margin:0;
    font-family:"Cinzel",serif;font-weight:500;
    font-size:66px;line-height:82px;color:var(--gold);
  }
  .lead{
    position:absolute;left:580px;top:608px;margin:0;width:600px;
    font-family:"Montserrat",sans-serif;font-weight:400;
    font-size:41px;line-height:68px;color:var(--text);
  }
  .phone-pill{
    position:absolute;left:120px;top:1060px;width:350px;height:56px;
    box-sizing:border-box;border:2px solid var(--gold);border-radius:30px;
    display:flex;align-items:center;justify-content:center;gap:14px;
    font-family:"Montserrat",sans-serif;font-size:28px;color:var(--text);
  }
  .brand{
    position:absolute;left:830px;top:1030px;display:flex;align-items:center;gap:18px;
    font-family:"Montserrat",sans-serif;font-weight:500;color:var(--gold);
  }
  .brand-mark{width:84px;height:84px;border:2px solid var(--gold);border-radius:50%;box-sizing:border-box;}
  .brand-name{display:flex;flex-direction:column;line-height:1;}
  .brand-name .main{font-size:33px;letter-spacing:1px;}
  .brand-name .sub{font-size:11px;letter-spacing:2.5px;margin-top:8px;}
</style>
</head>
<body>
<main class="post">
  <div class="backdrop" role="img" aria-label="Fundo desfocado de escritório com notebook e mesa"></div>
  <div class="accent-square"></div>
  <svg class="accent-dots" width="50" height="40" viewBox="0 0 50 40" aria-hidden="true">
    <rect x="0" y="0" width="34" height="34" fill="#c9ad8a"/>
    <rect x="28" y="20" width="16" height="16" fill="#8c6a40"/>
  </svg>
  <div class="hero-photo" role="img" aria-label="Foto de um pote de vidro cheio de moedas com uma pequena árvore crescendo dele"></div>

  <h1 class="headline">Somos<br>especialistas<br>em direito<br>previdênciário!</h1>
  <p class="lead">Oferecemos assessoria<br>jurídica completa,<br>apresentando soluções<br>seguras e eficientes</p>

  <div class="phone-pill">
    <svg width="28" height="28" viewBox="0 0 24 24" aria-hidden="true">
      <path d="M6.6 10.8a15.1 15.1 0 0 0 6.6 6.6l2.2-2.2a1 1 0 0 1 1-.25 11.4 11.4 0 0 0 3.6.57 1 1 0 0 1 1 1V20a1 1 0 0 1-1 1A17 17 0 0 1 3 4a1 1 0 0 1 1-1h3.5a1 1 0 0 1 1 1c0 1.25.2 2.45.57 3.57a1 1 0 0 1-.25 1z" fill="#2e2e2e"/>
    </svg>
    <span>(00) 0 0000.0000</span>
  </div>

  <div class="brand">
    <div class="brand-mark"></div>
    <div class="brand-name">
      <span class="main">RICARDO<br>ALMEIDA</span>
      <span class="sub">ADVOGADOS ASSOCIADOS</span>
    </div>
  </div>
</main>
</body>
</html>
```